Book cover design for the book titled "Quieter Under Lanterns."

create a book cover. The book title is, "Quieter Under Lanterns: A Ledger of Harbour Songs Across Mild Winters." The purpose of the book is to create awareness of how childhood trauma is impacting 7 out of 10 adults in the world today and that two-thirds of children will experience neglect and or abuse before their 18th birthday. One victim described that his mental and physical illness resulting from childhood trauma felt like he wa being pulled to the ground, that the force was "quieter under lanterns." The design should be clean and simple and communicate a crisis.

```html
<!DOCTYPE html>
<html lang="en">
<head>
<meta charset="utf-8">
<title>Quieter Under Lanterns — Cover Spread</title>
<link href="https://fonts.googleapis.com/css2?family=Raleway:wght@200&family=Arimo:wght@400;700&family=Amatic+SC:wght@700&display=swap" rel="stylesheet">
<style>
  :root {
    --paper: #ffffff;
    --ink: #000000;
    --photo-dark: #0b0b0b;
    --photo-mid: #3a3a3a;
    --photo-light: #9a9a9a;
    --silver-dark: #5e5e5e;
    --silver-light: #f2f2f2;
  }
  html, body {
    margin: 0;
    width: 1200px;
    height: 1200px;
    overflow: hidden;
    background: var(--paper);
  }
  .canvas { position: relative; width: 1200px; height: 1200px; }

  .back-cover {
    position: absolute; left: 94px; top: 274px; width: 476px; height: 696px;
    background: var(--ink);
  }
  .back-photo {
    position: absolute; left: 121px; top: 0; width: 255px; height: 223px;
    background: radial-gradient(ellipse 45% 60% at 50% 28%, var(--photo-light), var(--photo-mid) 45%, var(--photo-dark) 90%);
  }
  .blurb-frame {
    position: absolute; left: 56px; top: 223px; width: 362px; height: 436px;
    border: 2px solid var(--paper); background: var(--ink);
  }

  .spine {
    position: absolute; left: 570px; top: 274px; width: 80px; height: 696px;
    background: var(--paper);
  }
  .spine-title {
    position: absolute; left: 40px; top: 348px; width: 560px;
    transform: translate(-50%, -50%) rotate(-90deg);
    text-align: center; white-space: nowrap; color: var(--ink);
    font-size: 37px; line-height: 1;
  }
  .thin { font-family: "Raleway", sans-serif; font-weight: 200; }
  .bold { font-family: "Arimo", sans-serif; font-weight: 700; }

  .front-cover {
    position: absolute; left: 650px; top: 274px; width: 474px; height: 696px;
    background: var(--ink); overflow: hidden;
  }
  .front-photo {
    position: absolute; left: 228px; top: 296px; width: 246px; height: 376px;
    background: radial-gradient(ellipse 50% 55% at 52% 42%, var(--photo-light), var(--photo-mid) 45%, var(--photo-dark) 92%);
  }
  .title-block {
    position: absolute; left: 41px; top: 91px; width: 389px; height: 149px;
    background: var(--paper);
  }
  .title-top {
    position: absolute; left: 0; top: 8px; width: 100%;
    text-align: center; font-size: 44px; line-height: 1; color: var(--ink);
    letter-spacing: -1px;
  }
  .title-main {
    position: absolute; left: 6px; top: 59px; width: 377px; height: 85px;
    background: var(--ink); color: var(--paper);
    display: flex; align-items: center; justify-content: center;
    font-size: 62px; letter-spacing: 1px;
  }
  .subtitle {
    position: absolute; left: 60px; top: 280px; width: 380px;
    font-family: "Amatic SC", sans-serif; font-weight: 700;
    color: var(--paper); font-size: 38px; line-height: 1.15;
  }
  .subtitle span { display: block; }
  .subtitle .line-1 { padding-left: 30px; }
  .query-mark {
    position: absolute; font-family: "Arimo", sans-serif; color: var(--paper);
    line-height: 1;
  }
  .author-band {
    position: absolute; left: 1px; top: 623px; width: 473px; height: 49px;
    background: linear-gradient(90deg, var(--silver-dark), var(--silver-light) 45%, var(--silver-light) 60%, var(--silver-dark));
    display: flex; align-items: center; justify-content: center;
    font-family: "Arimo", sans-serif; font-weight: 400; font-size: 33px;
    color: var(--ink); padding-left: 20px; box-sizing: border-box;
  }
</style>
</head>
<body>
<div class="canvas">
  <section class="back-cover">
    <div class="back-photo" role="img" aria-label="Black and white photo of a lone figure seated on a stool against a dim wooden wall"></div>
    <div class="blurb-frame"></div>
  </section>

  <section class="spine">
    <div class="spine-title"><span class="thin">QUIETER UNDER </span><span class="bold">LANTERNS</span></div>
  </section>

  <section class="front-cover">
    <div class="front-photo" role="img" aria-label="Black and white photo of a lone figure seated on a stool, head bowed, under a single light"></div>
    <div class="title-block">
      <div class="title-top thin">QUIETER UNDER</div>
      <div class="title-main bold">LANTERNS</div>
    </div>
    <div class="subtitle">
      <span class="line-1">A LEDGER OF HARBOUR SONGS</span>
      <span class="line-2">ACROSS MILD WINTERS.</span>
    </div>
    <span class="query-mark" style="left:383px;top:342px;font-size:50px;transform:rotate(10deg);">?</span>
    <span class="query-mark" style="left:272px;top:375px;font-size:48px;transform:rotate(-20deg);">?</span>
    <span class="query-mark" style="left:405px;top:400px;font-size:30px;transform:rotate(15deg);">?</span>
    <span class="query-mark" style="left:295px;top:505px;font-size:28px;">?</span>
    <div class="author-band">AUTHOR NAME</div>
  </section>
</div>
</body>
</html>
```